Tile installation contractor -business card design

We are a tile contractor doing installation of tile on floors, walls, we tile showers, backsplashes, kitchens, entry ways. we install all types of tile ceramic, porcelain, travertine, marble, slate ect. we also do demolition and tear outs of old existing tile (removal) we do commercial, or residential jobs. tile and grout repairs. sealing of grout/tile. small or large jobs. we are fast, clean, do quality work, honest and hard working. anything tile we can do. design or patterns. we do shower pans and all prep work needed to install tile. fair competitive pricing
Industry/Entity Type
Business
Contact Information for Business Card
Granvale Tile- company name
Dean Ruskin/ owner 801-555-2943
granvale_tile@quormail.net
Free Estimates
Clinton Utah, 84099
20+ years experience
Licensed and Insured

```html
<!DOCTYPE html>
<html lang="en">
<head>
<meta charset="utf-8">
<title>Granvale Tile – Business Card</title>
<link href="https://fonts.googleapis.com/css2?family=Montserrat:wght@700&family=Didact+Gothic&display=swap" rel="stylesheet">
<style>
  :root {
    --backdrop: #2b2b2d;
    --card: #25272a;
    --grey: #8e8e8e;
    --grey-light: #9a9a9a;
    --green: #9acd32;
  }
  * { margin: 0; padding: 0; box-sizing: border-box; }
  html, body { width: 1200px; height: 1189px; overflow: hidden; background: var(--backdrop); }
  .canvas { position: relative; width: 1200px; height: 1189px; }
  .card {
    position: absolute; left: 150px; width: 900px; height: 514px;
    background: var(--card); border-radius: 26px;
    box-shadow: 0 10px 30px rgba(0,0,0,.45);
    overflow: hidden;
  }
  .card--front { top: 50px; }
  .card--back { top: 625px; }

  /* Front */
  .brand {
    position: absolute; left: 0; right: 0; top: 190px;
    display: flex; align-items: center; justify-content: center; gap: 26px;
  }
  .brand__mark { width: 64px; height: 64px; background: var(--green); }
  .brand__name {
    font-family: "Montserrat", sans-serif; font-weight: 700;
    font-size: 76px; color: var(--grey); letter-spacing: 1px; line-height: 1;
  }
  .tagline {
    position: absolute; left: 0; right: 0; top: 320px; text-align: center;
    font-family: "Didact Gothic", sans-serif; font-size: 27px;
    color: var(--grey); letter-spacing: 1px;
  }
  .tagline .sep { color: var(--green); margin: 0 14px; }

  /* Back */
  .back-brand {
    position: absolute; left: 60px; top: 0; width: 330px; height: 514px;
    display: flex; flex-direction: column; align-items: center; justify-content: center; gap: 24px;
  }
  .back-brand__mark { width: 110px; height: 110px; background: var(--green); }
  .back-brand__name {
    font-family: "Montserrat", sans-serif; font-weight: 700;
    font-size: 40px; color: var(--grey); line-height: 1;
  }
  .divider {
    position: absolute; left: 430px; top: 90px; width: 2px; height: 330px;
    background: var(--green);
  }
  .person { position: absolute; left: 500px; top: 95px; }
  .person__name {
    font-family: "Montserrat", sans-serif; font-weight: 700;
    font-size: 30px; color: var(--grey); line-height: 1;
  }
  .person__role {
    font-family: "Montserrat", sans-serif; font-weight: 700;
    font-size: 22px; color: var(--green); line-height: 1.1;
  }
  .contacts { position: absolute; left: 500px; top: 290px; list-style: none; }
  .contacts li {
    display: flex; align-items: center; gap: 12px; margin-bottom: 8px;
    font-family: "Didact Gothic", sans-serif; font-size: 27px;
    color: var(--grey-light); line-height: 1;
  }
  .contacts .icon {
    width: 30px; height: 30px; border-radius: 5px; background: var(--green);
    display: flex; align-items: center; justify-content: center; flex: none;
  }
  .contacts svg { width: 20px; height: 20px; }
</style>
</head>
<body>
<main class="canvas">

  <section class="card card--front" aria-label="Card front">
    <div class="brand">
      <span class="brand__mark"></span>
      <h1 class="brand__name">Granvale Tile</h1>
    </div>
    <p class="tagline">Free Estimates<span class="sep">|</span>20+ years experience<span class="sep">|</span>Licensed and Insured</p>
  </section>

  <section class="card card--back" aria-label="Card back">
    <div class="back-brand">
      <span class="back-brand__mark"></span>
      <span class="back-brand__name">Granvale Tile</span>
    </div>
    <div class="divider"></div>
    <div class="person">
      <p class="person__name">Dean Ruskin</p>
      <p class="person__role">owner</p>
    </div>
    <ul class="contacts">
      <li>
        <span class="icon"><svg viewBox="0 0 24 24"><path fill="#25272a" d="M6.6 10.8a15.1 15.1 0 0 0 6.6 6.6l2.2-2.2c.3-.3.7-.4 1-.2 1.1.4 2.3.6 3.6.6.6 0 1 .4 1 1V20c0 .6-.4 1-1 1A17 17 0 0 1 3 4c0-.6.4-1 1-1h3.5c.6 0 1 .4 1 1 0 1.3.2 2.5.6 3.6.1.3 0 .7-.2 1z"/></svg></span>
        801-555-2943
      </li>
      <li>
        <span class="icon"><svg viewBox="0 0 24 24"><rect x="3" y="5" width="18" height="14" rx="1" fill="none" stroke="#25272a" stroke-width="2"/><path d="M3 6l9 7 9-7" fill="none" stroke="#25272a" stroke-width="2"/></svg></span>
        granvale_tile@quormail.net
      </li>
      <li>
        <span class="icon"><svg viewBox="0 0 24 24"><path fill="#25272a" d="M12 2a7 7 0 0 0-7 7c0 5 7 13 7 13s7-8 7-13a7 7 0 0 0-7-7zm0 9.5A2.5 2.5 0 1 1 12 6.5a2.5 2.5 0 0 1 0 5z"/></svg></span>
        Harlow Springs, 84099
      </li>
    </ul>
  </section>

</main>
</body>
</html>
```